Flyer Design

I recently got a website designed by Pagecraft - www.tidynestliving.com.au

I own an organisational business. We help people to simplify their homes which in turn, creates a more balanced and healthy life. We offer de-clutter services for pantries, wardrobes, linen cupboards, home offices, and anywhere you need a bit of organisation. We can help you with de-cluttering and property styling that will help to sell your home. In addition, we provide help with moving, packing and unpacking, or even downsizing. With our keen eye for detail and passion for interior design, we will not only provide a practical solution, but a wonderful design element to your home. Tidy Nest Living is a proud member of the Southern Guild of Certified Space Planners Inc.

Can I please use the logo off my website. I have also put it below.

Industry/Entity Type

Business

```html
<!DOCTYPE html>
<html lang="en">
<head>
<meta charset="utf-8">
<title>Tidy Nest Living – Flyer</title>
<link rel="stylesheet" href="https://fonts.googleapis.com/css2?family=PT+Sans:ital,wght@0,400;0,700;1,400&family=PT+Sans+Narrow:wght@400;700&display=swap">
<style>
  :root{
    --stage:#e6e7e8;
    --charcoal:#2e3439;
    --charcoal-deep:#1f2427;
    --teal:#5fb3bd;
    --ring:#44535c;
    --ice:#c9dce5;
    --ice-light:#e3eef3;
    --navy:#1a2638;
    --navy-deep:#0f1826;
    --accent:#2a8fd0;
    --ink:#2a3340;
    --pale:#d9dde0;
  }
  *{box-sizing:border-box;margin:0;padding:0}
  html,body{width:1200px;height:900px;overflow:hidden;background:var(--stage)}
  .canvas{position:relative;width:1200px;height:900px}
  .flyer{position:absolute;top:140px;width:420px;height:600px;overflow:hidden;box-shadow:0 6px 18px rgba(0,0,0,.35)}
  .flyer--front{left:150px;background:linear-gradient(170deg,var(--charcoal) 0%,var(--charcoal-deep) 100%);border-right:4px solid var(--accent)}
  .flyer--back{left:630px;background:var(--navy)}
  .front-photos{position:absolute;left:0;top:0}
  .brand{position:absolute;display:flex;align-items:center;gap:10px;font-family:"PT Sans",sans-serif;font-weight:700;color:var(--teal);letter-spacing:.5px;white-space:nowrap}
  .brand-mark{width:22px;height:22px;background:var(--teal)}
  .flyer--front .brand{left:70px;top:350px;font-size:26px}
  .front-copy{position:absolute;left:70px;right:20px;top:410px;font-family:"PT Sans Narrow",sans-serif;color:var(--pale);text-transform:uppercase}
  .front-title{font-weight:700;font-size:12.5px;margin-bottom:14px;color:#fff}
  .front-copy p{font-size:8.6px;line-height:1.45;margin-bottom:8px}
  .front-web{position:absolute;right:22px;bottom:22px;font-family:"PT Sans Narrow",sans-serif;font-weight:700;font-size:14px;color:#e8ecee}
  .back-photo{position:absolute;left:0;top:0}
  .flyer--back .brand{right:14px;top:104px;font-size:18px}
  .back-panel{position:absolute;left:0;top:150px;width:420px;height:314px;background:linear-gradient(180deg,var(--ice-light) 0%,var(--ice) 100%);border-bottom:4px solid var(--accent)}
  .back-copy{position:absolute;left:60px;right:72px;top:156px;font-family:"PT Sans",sans-serif;font-style:italic;color:var(--ink)}
  .back-title{font-style:normal;font-weight:700;font-size:11px;margin-bottom:10px}
  .back-copy p{font-size:8.6px;line-height:1.35;margin:0 0 7px 20px}
  .back-copy p:last-child{margin-bottom:0}
  .badge{position:absolute;right:20px;top:412px;width:40px;height:50px;background:#fff;border:1px solid #777}
  .back-footer{position:absolute;left:0;top:468px;width:420px;height:132px;background:linear-gradient(180deg,var(--navy) 0%,var(--navy-deep) 100%);font-family:"PT Sans",sans-serif;color:#c8d3de}
  .footer-name{position:absolute;left:40px;top:18px;font-size:11px}
  .footer-contact{position:absolute;left:40px;top:56px;font-size:11px;line-height:1.5}
  .footer-hours{position:absolute;left:140px;top:100px;font-size:11px}
</style>
</head>
<body>
<main class="canvas">
  <article class="flyer flyer--front">
    <svg class="front-photos" width="420" height="340" viewBox="0 0 420 340">
      <path role="img" aria-label="Photo of tidy bookshelves with books, letter blocks and storage trays" d="M0 40 H300 A130 130 0 0 1 330 280 A150 150 0 0 1 40 300 L0 300 Z" fill="#7a6a5a" stroke="var(--ring)" stroke-width="10"/>
      <circle cx="275" cy="90" r="55" fill="#c9d8e3" stroke="var(--ring)" stroke-width="8" role="img" aria-label="Photo of a neatly arranged craft storage room"/>
      <circle cx="292" cy="215" r="40" fill="#8b7a8c" stroke="var(--ring)" stroke-width="8" role="img" aria-label="Photo of shirts hanging in an organised wardrobe"/>
    </svg>
    <div class="brand"><span class="brand-mark"></span>Tidy Nest Living</div>
    <div class="front-copy">
      <h2 class="front-title">Uncluttering life – one home at a time</h2>
      <p>At Tidy Nest Living, it is our goal to unclutter life, one house at a time. Whether you are planning a move and need to downsize, or you just need some basic organisation and storage, we are here for you, every step of the way.</p>
      <p>We help people to simplify their homes which in turn, creates a more balanced and healthy life. We put into place basic organisation systems that work for you and your family. We customise solutions to your unique needs, ensuring that your home offers practical yet attractive storage. Phone us today to schedule a consultation!</p>
      <p>When you are ready to live life de-cluttered, we are ready to help.</p>
    </div>
    <div class="front-web">WWW.TIDYNESTLIVING.COM.AU</div>
  </article>

  <article class="flyer flyer--back">
    <svg class="back-photo" width="420" height="260" viewBox="0 0 420 260">
      <rect role="img" aria-label="Photo of white cube shelving filled with magazines and books" width="420" height="160" fill="#d8d2c8"/>
      <circle cx="30" cy="190" r="75" fill="#cfc8bb" stroke="var(--accent)" stroke-width="4" role="img" aria-label="Photo of an organised pantry shelf"/>
    </svg>
    <div class="back-panel"></div>
    <div class="brand"><span class="brand-mark"></span>Tidy Nest Living</div>
    <div class="back-copy">
      <h2 class="back-title">Organising Your Life</h2>
      <p>At Tidy Nest Living, we help you to organise your life. We work with busy working families who do not typically have time to organise their homes.</p>
      <p>We offer de-clutter services for pantries, wardrobes, linen cupboards, home offices, and anywhere you need a bit of organisation.</p>
      <p>We can help you with de-cluttering and property styling that will help to sell your home. In addition, we provide help with moving, packing and unpacking, or even downsizing.</p>
      <p>With our keen eye for detail and passion for interior design, we will not only provide a practical solution, but a wonderful design element to your home.</p>
      <p>Rates - $150 for the first 2 hours (minimum), $60 per hour thereafter. Travel Fee may apply. You will be surprised how much can be accomplished in a small amount of time!</p>
      <p>Let us put together a package to suit your needs.</p>
      <p>Tidy Nest Living is a proud member of the Southern Guild of Certified Space Planners Inc.</p>
    </div>
    <div class="badge" role="img" aria-label="Membership badge"></div>
    <footer class="back-footer">
      <div class="footer-name">Tidy Nest Living</div>
      <div class="footer-contact">Phone: 0400 123 456<br>Email: hello@tidynestliving.com.au</div>
      <div class="footer-hours">Business Hours By Appointment Only</div>
    </footer>
  </article>
</main>
</body>
</html>
```